Vehicle wrap design

I need a vehicle wrap design for my tree care company. I would like to keep my original logo in there and keep the colours. The wrap will be going on the truck in the pic attached.

www.bouldercrestgrove.nz

Target Market(s)

Home service

Industry/Entity Type

Arboriculture

Requirements
Must have
• I would like to keep a lot of white to keep the wrap price down.

```html
<!DOCTYPE html>
<html lang="en">
<head>
<meta charset="utf-8">
<title>Bouldercrestgrove vehicle wrap</title>
<link href="https://fonts.googleapis.com/css2?family=Montserrat:wght@600;700&display=swap" rel="stylesheet">
<style>
:root{
  --orange:#e2600f;
  --blue:#2e3a8f;
  --white:#ffffff;
  --backdrop:#e8ebef;
  --edge:#d3d7de;
}
*{margin:0;padding:0;box-sizing:border-box}
html,body{width:1200px;height:530px;overflow:hidden;background:var(--backdrop);font-family:"Montserrat",sans-serif}
.canvas{position:relative;width:1200px;height:530px}
.panel{position:absolute;background:var(--white);border:1px solid var(--edge);overflow:hidden}
.brand-mark{position:absolute;border-radius:50%;background:var(--orange)}
.brand-name{position:absolute;left:0;right:0;text-align:center;font-weight:700;color:var(--blue);white-space:nowrap}

/* cab */
.cab{position:absolute;left:36px;top:125px;width:210px;height:236px}
.cab-brand{position:absolute;left:36px;top:125px;width:150px;height:200px}
.cab-brand .brand-mark{left:60px;top:120px;width:28px;height:28px}
.cab-brand .brand-name{top:154px;font-size:8.5px;font-weight:600}

/* side: services */
.side-services{left:247px;top:142px;width:110px;height:184px}
.side-services ul{list-style:none;padding:34px 0 0 0;text-align:center}
.side-services li{font-size:8.4px;font-weight:700;color:var(--blue);line-height:9px;margin-bottom:11.5px}
.side-services li::before{content:"";display:inline-block;width:4px;height:4px;border-radius:50%;background:var(--orange);margin-right:3px;vertical-align:middle}

/* side: main box */
.side-main{left:370px;top:67px;width:352px;height:266px}
.side-main .brand-mark{left:126px;top:22px;width:100px;height:100px}
.side-main .brand-name{top:130px;font-size:25px;letter-spacing:-.3px}

.phone{position:absolute;display:flex;align-items:center;justify-content:center;gap:6px;color:var(--orange);font-weight:700;white-space:nowrap}
.phone svg{fill:var(--blue)}
.side-main .phone{left:0;right:0;top:172px;font-size:26px}

.stripe{position:absolute;left:0;right:0;height:5px;background:var(--orange)}
.band{position:absolute;left:0;right:0;bottom:0;background:var(--blue);display:flex;align-items:center;justify-content:center}
.url{color:var(--white);font-weight:600;letter-spacing:1.4px}
.side-main .stripe{top:217px}
.side-main .band{top:223px}
.side-main .url{font-size:14px}

/* rear */
.rear{left:778px;top:161px;width:383px;height:228px}
.rear-divider{position:absolute;left:200px;top:0;width:2px;height:155px;background:var(--edge)}
.rear-brand{position:absolute;left:0;top:0;width:200px;height:155px}
.rear-brand .brand-mark{left:60px;top:18px;width:80px;height:80px}
.rear-brand .brand-name{top:112px;font-size:13.5px}
.rear-services{position:absolute;left:202px;right:0;top:22px;list-style:none;text-align:center}
.rear-services li{font-size:11px;font-weight:700;color:var(--blue);line-height:16.5px}
.rear-services li::before{content:"";display:inline-block;width:5px;height:5px;border-radius:50%;background:var(--orange);margin-right:5px;vertical-align:middle}
.rear .phone{left:202px;right:0;top:104px;font-size:20px}
.rear .stripe{top:155px}
.rear .band{top:161px}
.rear .url{font-size:17px;letter-spacing:1.6px}
</style>
</head>
<body>
<div class="canvas">

  <svg class="cab" viewBox="0 0 210 236" aria-hidden="true">
    <path d="M0 40 Q4 6 40 2 L200 2 L200 236 L0 236 Z" fill="var(--white)" stroke="var(--edge)"/>
    <path d="M200 160 L88 160 Q60 162 50 190 L30 236 L46 236 L62 198 Q70 172 96 170 L200 170 Z" fill="var(--orange)"/>
    <path d="M200 172 L100 172 Q76 174 68 200 L54 236 L86 236 L96 210 Q104 194 122 194 L200 194 Z" fill="var(--blue)"/>
  </svg>
  <div class="cab-brand">
    <span class="brand-mark"></span>
    <span class="brand-name">BOULDERCRESTGROVE</span>
  </div>

  <div class="panel side-services">
    <ul>
      <li>TREE<br>PRUNING</li>
      <li>TREE<br>REMOVAL</li>
      <li>STUMP<br>GRINDING</li>
      <li>HEDGE<br>TRIMMING</li>
      <li>TREE<br>MULCHING</li>
    </ul>
  </div>

  <div class="panel side-main">
    <span class="brand-mark"></span>
    <span class="brand-name">BOULDERCRESTGROVE</span>
    <div class="phone">
      <svg width="22" height="22" viewBox="0 0 24 24" aria-hidden="true"><path d="M6.6 10.8a15.1 15.1 0 0 0 6.6 6.6l2.2-2.2a1 1 0 0 1 1-.25 11.4 11.4 0 0 0 3.6.57 1 1 0 0 1 1 1V20a1 1 0 0 1-1 1A17 17 0 0 1 3 4a1 1 0 0 1 1-1h3.5a1 1 0 0 1 1 1c0 1.25.2 2.45.57 3.57a1 1 0 0 1-.25 1z"/></svg>
      <span>0275550143</span>
    </div>
    <div class="stripe"></div>
    <div class="band"><span class="url">WWW.BOULDERCRESTGROVE.NZ</span></div>
  </div>

  <div class="panel rear">
    <div class="rear-divider"></div>
    <div class="rear-brand">
      <span class="brand-mark"></span>
      <span class="brand-name">BOULDERCRESTGROVE</span>
    </div>
    <ul class="rear-services">
      <li>TREE PRUNING</li>
      <li>TREE REMOVAL</li>
      <li>STUMP GRINDING</li>
      <li>HEDGE TRIMMING</li>
      <li>TREE MULCHING</li>
    </ul>
    <div class="phone">
      <svg width="16" height="16" viewBox="0 0 24 24" aria-hidden="true"><path d="M6.6 10.8a15.1 15.1 0 0 0 6.6 6.6l2.2-2.2a1 1 0 0 1 1-.25 11.4 11.4 0 0 0 3.6.57 1 1 0 0 1 1 1V20a1 1 0 0 1-1 1A17 17 0 0 1 3 4a1 1 0 0 1 1-1h3.5a1 1 0 0 1 1 1c0 1.25.2 2.45.57 3.57a1 1 0 0 1-.25 1z"/></svg>
      <span>0275550143</span>
    </div>
    <div class="stripe"></div>
    <div class="band"><span class="url">WWW.BOULDERCRESTGROVE.NZ</span></div>
  </div>

</div>
</body>
</html>
```